依頼詳細

■デザインイメージ
─────────────────────────────────────

1.添付のPPTファイルを参考に、ご提案を1枚作成いただきたいです。
2.デザイン上、文字や図の配置は素案から変更していただいて一向に結構ですが、
タイトルの文字の大きさや位置(一番上)は、10m先からタイトル文字が見えるようにし
たいので、それが適う範囲でデザインをお願いします。
3.セキュリティ製品を取り扱っているので、セキュリティをイメージできるもの。
4.製品マーク(盾)は必ず使用してください。
5.提案いただいたデザインと類似デザインで、残りの2~3枚をご制作いただく想定です。

■ 入稿詳細
作成ファイル :イラストレータファイル(EPS)
Illustrator CS5まで
サイズ : A1(パネル 594 × 841mm)
記載項目
添付のPPTをご参照ください。
希望イメージ
シンプル 複雑
単色 カラフル
暗い 明るい
日常 高級
遊び心 厳粛
未来的 伝統的
女性的 男性的
希望する色
緑・黒を基調としたもの
納品ファイル
• イラストレーター形式 (.ai)
補足説明

※9月30日にはパネル制作へ入稿を予定、
コンペ(1枚目)・プロジェクト(2~3枚)共にご対応いただける方を希望します。

以上となります。
宜しくお願い致します。
提案予約をいただいている方が、複数名いらっしゃいますので、
1日締め切りを延ばさせていただきます。
■ 選んだ理由

固いイメージを保ちつつ、シンプルな印象で
あまり、懲りすぎていないデザインがよかったため、
こちらのデザインを選定させていただきました。

また、緑色を多用しすぎていないところも気に入りました。

■ 提案者全員のお礼・コメント

どの方のデザインもとても素敵で、
選定に悩みました。

たくさんのデザインをご提案いただき、
誠に有難う御座いました。

```html
<!DOCTYPE html>
<html lang="ja">
<head>
<meta charset="utf-8">
<title>SYLVA 自動監査システム</title>
<link href="https://fonts.googleapis.com/css2?family=Noto+Sans+JP:wght@400;700;900&display=swap" rel="stylesheet">
<style>
:root{
  --black:#050806;
  --deep:#0b1f10;
  --green:#2f9a3a;
  --green-dark:#17551f;
  --green-light:#7fdc58;
  --yellow:#f4e24a;
  --white:#ffffff;
  --red:#d8201c;
  --grey:#c9d3cb;
}
*{margin:0;padding:0;box-sizing:border-box}
html,body{width:860px;height:1200px;overflow:hidden;background:var(--black)}
body{font-family:"Noto Sans JP",sans-serif;color:var(--white)}
.poster{position:relative;width:860px;height:1200px;overflow:hidden;
  background:radial-gradient(ellipse at 50% 108%,#3fae3a 0%,#14491a 28%,var(--black) 55%),var(--black)}
.top-band{height:58px;background:var(--black);display:flex;align-items:center;justify-content:center;
  color:var(--green-light);font-weight:900;font-size:25px;letter-spacing:1px;border-bottom:2px solid var(--green-dark)}
.hero{position:relative;height:352px;
  background:radial-gradient(ellipse at 60% 40%,#1f5f22 0%,#0d2810 45%,var(--black) 80%)}
.brand{position:absolute;left:44px;top:70px;display:flex;align-items:center;gap:10px;
  font-weight:900;font-size:40px;color:var(--yellow)}
.brand-square{width:30px;height:30px;background:var(--yellow)}
.title{position:absolute;left:290px;top:22px;font-weight:900;font-size:112px;line-height:122px;
  color:var(--white);letter-spacing:4px;-webkit-text-stroke:3px var(--black);
  text-shadow:0 0 0 var(--black),4px 4px 0 var(--black)}
.tagline{position:absolute;left:40px;top:282px;display:flex;align-items:center;gap:8px}
.tag{background:var(--green);border:2px solid var(--green-light);font-weight:900;font-size:26px;
  padding:0 12px;line-height:44px;color:var(--white)}
.tag-main{margin-left:18px;font-weight:900;font-size:46px;color:var(--white);letter-spacing:2px}
.section-head{margin:14px 40px 0;height:50px;display:flex;align-items:center;justify-content:center;
  background:linear-gradient(180deg,#3fb043,#1b6d22);border-top:2px solid var(--green-light);
  color:var(--yellow);font-weight:900;font-size:25px}
.body-text{margin:12px 50px 0;font-size:12.5px;line-height:21px;color:var(--grey)}
.feature-grid{margin:14px 40px 0;display:grid;grid-template-columns:repeat(4,1fr);gap:8px}
.feature{height:58px;background:linear-gradient(180deg,#2e8d33,#17591c);border:1px solid var(--green-light);
  display:flex;flex-direction:column;align-items:center;justify-content:center;
  font-weight:700;font-size:16px;line-height:21px;text-align:center}
.section-head.second{margin-top:30px}
.flow{position:absolute;left:0;top:880px;width:860px;height:320px}
.art{position:absolute;border-radius:6px}
.art-server-left{left:80px;top:40px;width:110px;height:150px;background:linear-gradient(180deg,#3a3a3a,#111)}
.art-server-right{left:690px;top:40px;width:110px;height:150px;background:linear-gradient(180deg,#3a3a3a,#111)}
.art-mail{left:370px;top:170px;width:120px;height:70px;background:linear-gradient(180deg,#f2f2f2,#b9b9b9)}
.flow-label{position:absolute;top:70px;width:110px;height:86px;background:var(--white);color:var(--green-dark);
  border:3px solid var(--green);font-weight:900;font-size:21px;line-height:28px;
  display:flex;align-items:center;justify-content:center;text-align:center}
.label-log{left:200px}
.label-policy{left:560px}
.check{position:absolute;left:310px;top:84px;width:250px;height:56px;background:var(--white);
  color:var(--green-dark);font-weight:900;font-size:23px;display:flex;align-items:center;justify-content:center;
  clip-path:polygon(0 50%,12% 0,12% 20%,88% 20%,88% 0,100% 50%,88% 100%,88% 80%,12% 80%,12% 100%)}
.alert{position:absolute;left:310px;top:180px;width:240px;height:130px}
.alert-text{position:absolute;left:0;top:0;width:240px;height:130px;display:flex;align-items:center;
  justify-content:center;text-align:center;font-weight:900;font-size:24px;line-height:30px;color:var(--white)}
</style>
</head>
<body>
<div class="poster">
  <div class="top-band">サーバ・パソコン・DB・プログラム・ネットワーク</div>

  <div class="hero">
    <div class="brand"><span class="brand-square"></span>SYLVA</div>
    <h1 class="title">操作制御<br>ログ取得</h1>
    <div class="tagline">
      <span class="tag">簡単</span><span class="tag">安全</span><span class="tag">確実</span>
      <span class="tag-main">自動監査システム</span>
    </div>
  </div>

  <h2 class="section-head">エージェントによる徹底した操作制御とログ取得</h2>
  <p class="body-text">様々なプラットフォームのコンピュータに対応し、端末ごとの操作を細かく制御します。SYLVA Trace Agentの導入で、不正なデバイス接続やアプリケーションの実行をブロックし、すべての操作履歴を確実に記録します。取得したログは改ざんを防いだ状態で安全に保管され、監査や調査の際にすぐ活用できます。</p>

  <div class="feature-grid">
    <div class="feature"><span>コンピュータ</span><span>操作制御・ログ取得</span></div>
    <div class="feature"><span>データベース</span><span>アクセスログ取得</span></div>
    <div class="feature"><span>プログラム</span><span>変更ログ取得</span></div>
    <div class="feature"><span>マルウェア</span><span>Web改ざん検知</span></div>
    <div class="feature"><span>ファイルサーバ</span><span>アクセスログ取得</span></div>
    <div class="feature"><span>ネットワーク</span><span>パケット取得</span></div>
    <div class="feature"><span>サーバ 標準</span><span>イベントログ取得</span></div>
    <div class="feature"><span>CPU、メモリ、</span><span>HDD使用量取得</span></div>
  </div>

  <h2 class="section-head second">統合ログ管理マネージャによるログ一元化と自動監査システム</h2>
  <p class="body-text">収集したログはSYLVA Log Managerで一元管理され、監査ポリシーに基づいて自動でチェックされます。違反操作を検知すると管理者へ即時に通知し、レポートも自動で作成。運用の手間を大きく減らしながら、確実な監査を実現します。</p>

  <div class="flow">
    <div class="art art-server-left" role="img" aria-label="ログを蓄積するサーバのイラスト"></div>
    <div class="art art-server-right" role="img" aria-label="監査ポリシーを持つサーバのイラスト"></div>
    <div class="flow-label label-log">蓄積した<br>監査ログ</div>
    <div class="check">自動チェック</div>
    <div class="flow-label label-policy">監査<br>ポリシー</div>
    <div class="art art-mail" role="img" aria-label="通知メールの封筒のイラスト"></div>
    <div class="alert">
      <svg width="240" height="130" viewBox="0 0 240 130" aria-hidden="true">
        <polygon fill="#d8201c" stroke="#ffffff" stroke-width="3"
          points="120,4 140,30 180,10 178,40 232,38 200,62 236,88 186,90 196,124 150,104 120,128 92,104 44,124 54,92 4,88 40,64 8,38 60,40 58,10 100,30"/>
      </svg>
      <div class="alert-text">ポリシー違反<br>操作!</div>
    </div>
  </div>
</div>
</body>
</html>
```